Mortgage Lender needs Flyers Designed

We are a wholesale mortgage lender providing mortgage services throughout the United States to mortgage brokers. We just merged with a company and need to redesign their product flyers and matrices so they are more in line with a modern and sleek look. We provide residential and commercial mortgage financing options. I have attached a document labeled FULL STACK. This is the current flyer set that needs to be redesigned for my company. There are 10 programs featured in the document. The first two pages provide a product overview and the following 17 pages are the matrices for each product. I need a design set created in either Adobe Photoshop or Adobe Indesign so we can edit the content as necessary.

Target Market(s)

Mortgage Brokers in the United States

Industry/Entity Type

Finance, Mortgage

Font styles to use
Serif
Sans Serif

Requirements
Must have
• Must include all ten programs and must be designed using Adobe Photoshop or Adobe InDesign (preferred)
Nice to have
• Great graphics and clean modern feel.
Should not have
• Typos, hard to edit fields, should not look very similar to the FULL STACK pdf attached.

```html
<!DOCTYPE html>
<html lang="en">
<head>
<meta charset="utf-8">
<title>Ground Up Construction Program – The Northvale Group</title>
<link href="https://fonts.googleapis.com/css2?family=Merriweather:wght@400;700&family=Inter:wght@400;600;700&display=swap" rel="stylesheet">
<style>
  :root{
    --backdrop:#d7d6d7;
    --paper:#ffffff;
    --green:#446a35;
    --green-text:#3d6a33;
    --ink:#1d1d1d;
    --rule:#bdbdbd;
    --footer-fill:#e1e1e1;
  }
  *{box-sizing:border-box;margin:0;padding:0}
  html,body{width:1200px;height:856px;overflow:hidden;background:var(--backdrop)}
  body{position:relative;font-family:"Inter",Arial,sans-serif;color:var(--ink)}

  .sheet{position:absolute;top:58px;width:513px;height:724px;background:var(--paper);overflow:hidden}
  .sheet--terms{left:54px}
  .sheet--collateral{left:625px}

  .sheet__title{position:absolute;left:35px;top:24px;font-family:"Merriweather",Georgia,serif;font-weight:700;font-size:25px;line-height:30px;color:var(--ink);letter-spacing:-.2px}
  .sheet__rule{position:absolute;left:0;top:97px;width:292px;height:1px;background:#555}
  .sheet__rule-accent{position:absolute;left:35px;top:95px;width:52px;height:5px;border-radius:3px;background:var(--green)}
  .sheet__intro{position:absolute;left:35px;top:107px;font-family:"Merriweather",Georgia,serif;font-size:11.2px;line-height:15.5px;color:var(--green-text)}

  .brand{position:absolute;right:30px;top:62px;text-align:center}
  .brand__mark{display:block;width:26px;height:26px;margin:0 auto 8px;background:var(--green)}
  .brand__name{display:block;font-family:"Merriweather",Georgia,serif;font-weight:700;font-size:9px;letter-spacing:.1px;color:var(--ink);white-space:nowrap}

  .matrix{position:absolute;left:35px;top:148px;width:444px;border:1px dashed var(--green);border-radius:8px;overflow:hidden}
  .matrix table{width:100%;border-collapse:collapse;table-layout:fixed}
  .matrix td,.matrix th{vertical-align:top;font-size:5.9px;line-height:7px;font-weight:400;text-align:left;letter-spacing:-.05px}
  .col-section{width:112px}
  .col-label{width:101px}
  .col-ground{width:112px}

  .section{background:var(--green);color:#fff;font-weight:700;font-size:8.3px !important;line-height:10px !important;text-align:center !important;vertical-align:middle !important;padding:0 10px}
  .section--split{border-top:1px solid rgba(255,255,255,.35)}
  .head{color:var(--green-text);font-weight:700 !important;font-size:5.6px !important;line-height:6.4px !important;padding:6px 8px 0;border-left:1px solid var(--rule);border-bottom:1px solid var(--rule)}
  .head--blank{border-left:none}
  .label{padding:8px 6px 0 12px;border-bottom:1px solid var(--rule)}
  .cell{padding:6px 6px 0 6px;border-left:1px solid var(--rule);border-bottom:1px solid var(--rule)}
  .row-last .label,.row-last .cell{border-bottom:none}
  .middle td.label,.middle td.cell{vertical-align:middle;padding-top:0}

  .points{list-style:none}
  .points li{position:relative;padding-left:7px;margin-bottom:3.5px}
  .points li::before{content:"";position:absolute;left:0;top:2px;border-left:3px solid #333;border-top:1.6px solid transparent;border-bottom:1.6px solid transparent}
  .stack p{margin-bottom:3px}
  .types{line-height:10px !important;padding-top:4px !important}
  .types strong{font-weight:600;display:block}
  .types .gap{margin-top:3px}

  .sheet__footer{position:absolute;left:0;bottom:0;width:513px;height:100px}
  .sheet__site{position:absolute;left:0;right:0;bottom:16px;text-align:center;font-family:"Merriweather",Georgia,serif;font-size:11px;letter-spacing:3.2px;color:#333}
</style>
</head>
<body>

<section class="sheet sheet--terms">
  <h1 class="sheet__title">Ground Up<br>Construction Program</h1>
  <div class="brand"><span class="brand__mark"></span><span class="brand__name">THE NORTHVALE GROUP</span></div>
  <div class="sheet__rule"></div><div class="sheet__rule-accent"></div>
  <p class="sheet__intro">These represent general guidelines and loan terms<br>are subject to lender discretion</p>

  <div class="matrix">
    <table>
      <colgroup><col class="col-section"><col class="col-label"><col class="col-ground"><col></colgroup>
      <tr style="height:23px">
        <td class="section"></td>
        <th class="head head--blank"></th>
        <th class="head">Ground Up Program</th>
        <th class="head">Experienced Developer Program<br>(3+ Similar Past Projects)</th>
      </tr>
      <tr style="height:55px">
        <td class="section section--split">Loan Terms</td>
        <td class="label" style="padding-top:23px">Third Party Construction<br>Reports</td>
        <td class="cell"></td>
        <td class="cell" style="padding-top:14px"><ul class="points">
          <li>3rd party feasibility study for 3+ unit developments</li>
          <li>3rd party vendor to monitor draws for developments</li></ul></td>
      </tr>
      <tr style="height:52px">
        <td class="section section--split" rowspan="3">Guarantor<br>Requirements</td>
        <td class="label" style="padding-top:16px">Minimum Net Worth &amp;<br>Liquidity</td>
        <td class="cell" style="padding-top:16px"><ul class="points"><li>Minimum net worth of 10% of the loan amount</li></ul></td>
        <td class="cell"><ul class="points">
          <li>Minimum net worth of 10% of the loan amount</li>
          <li>Bank statements showing 10% of loan amount post-close liquidity for developments</li></ul></td>
      </tr>
      <tr style="height:88px">
        <td class="label">Experience</td>
        <td class="cell"><ul class="points">
          <li>Previous real estate experience required: 1-2 Ground ups</li>
          <li>GCs if experience if permits tie to Ground ups</li>
          <li>Guarantors with no experience permitted on a case by case basis</li></ul></td>
        <td class="cell"><ul class="points">
          <li>Previous real estate experience required: 3+ similar Ground-up builds + heavy rehabs with expansion, Professional development/builder.</li>
          <li>Guarantors with no experience permitted with experienced guarantor that meets the above experience criteria</li></ul></td>
      </tr>
      <tr class="row-last" style="height:48px">
        <td class="label">Profit Test</td>
        <td class="cell" colspan="2"><ul class="points"><li>Minimum 30% ROI<br>If fail, must pass 1.20 DSCR test on a market 30-year FRM</li></ul></td>
      </tr>
    </table>
  </div>

  <svg class="sheet__footer" viewBox="0 0 513 100" aria-hidden="true">
    <path d="M13 100 Q256 4 500 100 Z" fill="var(--footer-fill)"/>
    <path d="M13 100 Q256 0 500 100 Q256 8 13 100 Z" fill="#111"/>
  </svg>
  <p class="sheet__site">WWW.NORTHVALELEND.COM</p>
</section>

<section class="sheet sheet--collateral">
  <h1 class="sheet__title">Ground Up<br>Construction Program</h1>
  <div class="brand"><span class="brand__mark"></span><span class="brand__name">THE NORTHVALE GROUP</span></div>
  <div class="sheet__rule"></div><div class="sheet__rule-accent"></div>
  <p class="sheet__intro">These represent general guidelines and loan terms<br>are subject to lender discretion</p>

  <div class="matrix">
    <table>
      <colgroup><col class="col-section"><col class="col-label"><col class="col-ground"><col></colgroup>
      <tr style="height:23px">
        <td class="section"></td>
        <th class="head head--blank"></th>
        <th class="head">Ground Up Program</th>
        <th class="head">Experienced Developer Program<br>(3+ Similar Past Projects)</th>
      </tr>
      <tr class="middle" style="height:26px">
        <td class="section section--split" rowspan="4">Eligible Collateral</td>
        <td class="label">Loan Amount</td>
        <td class="cell stack" colspan="2"><p>Min: $50,000</p><p style="margin:0">Max: $5,000,000</p></td>
      </tr>
      <tr class="middle" style="height:27px">
        <td class="label">Property Count</td>
        <td class="cell stack"><p>Min: 1</p><p style="margin:0">Max: 2</p></td>
        <td class="cell stack"><p>Min: 1</p><p style="margin:0">Max: 10</p></td>
      </tr>
      <tr style="height:205px">
        <td class="label" style="vertical-align:middle;padding-top:0">Permitted Property Types</td>
        <td class="cell types" colspan="2">
          <strong>Eligible</strong>
          -Non-owner Occupied 1-4 unit<br>residential<br>-Townhomes<br>-Condos
          <strong class="gap">Ineligible</strong>
          -Mixed use properties<br>-5+ unit multifamily properties<br>-Condotels<br>-Co-ops/TICs<br>-Commercial Property<br>-Log Homes<br>-Properties Subject to Oil and/or<br>Gas Leases<br>-Operating Farms, Ranches, or<br>Orchards<br>-Vacation or Seasonal Rentals<br>-Rural properties
        </td>
      </tr>
      <tr class="middle" style="height:20px">
        <td class="label">Submarket Liquidity</td>
        <td class="cell" colspan="2">Top 90%, Top 10% case by case with potential LTC cuts</td>
      </tr>
      <tr style="height:84px">
        <td class="section section--split" rowspan="6">Loan Terms</td>
        <td class="label" style="vertical-align:middle;padding-top:0">Maximum Loan to Cost</td>
        <td class="cell"><ul class="points">
          <li>Up to 75% of the lower of land value or purchase price/60% if unpermitted, plus 100% of construction</li>
          <li>Max 85% of total project costs</li>
          <li>LTC Catch Up Draw to raise initial advance to 75% at approval of required plans/permits post-closing</li></ul></td>
        <td class="cell"><ul class="points">
          <li>Up to 75% of the lower of land value or purchase price/60% if unpermitted, plus 100% of construction</li>
          <li>Max 90% of total project costs</li>
          <li>LTC Catch Up Draw to raise initial advance to 75% at approval of required plans/permits post-closing</li></ul></td>
      </tr>
      <tr class="middle" style="height:15px">
        <td class="label">Maximum Loan to ARV</td>
        <td class="cell" colspan="2"><ul class="points"><li style="margin:0">Up to 70%</li></ul></td>
      </tr>
      <tr style="height:44px">
        <td class="label" style="padding-top:3px">Reserves/Escrows</td>
        <td class="cell" style="padding-top:3px"><ul class="points"><li>Interest Reserve: Minimum 1 month</li></ul></td>
        <td class="cell" style="padding-top:3px"><ul class="points"><li>Interest Reserve: Minimum 1 month,Minimum 6 months full boat IR funded with initial loan amount for 90% LTC loans</li></ul></td>
      </tr>
      <tr class="middle" style="height:22px">
        <td class="label">Term Length</td>
        <td class="cell"><ul class="points"><li style="margin:0">12 months, Up to 18 at Lender Discretion</li></ul></td>
        <td class="cell"><ul class="points"><li style="margin:0">12 months, Up to 24 at Lender Discretion</li></ul></td>
      </tr>
      <tr class="middle" style="height:17px">
        <td class="label">Recourse</td>
        <td class="cell" colspan="2"><ul class="points"><li style="margin:0">Full Recourse</li></ul></td>
      </tr>
      <tr class="middle row-last" style="height:18px">
        <td class="label">Minimum FICO</td>
        <td class="cell"><ul class="points"><li style="margin:0">680 Midscore</li></ul></td>
        <td class="cell"><ul class="points"><li style="margin:0">680 Midscore</li></ul></td>
      </tr>
    </table>
  </div>

  <svg class="sheet__footer" viewBox="0 0 513 100" aria-hidden="true">
    <path d="M13 100 Q256 4 500 100 Z" fill="var(--footer-fill)"/>
    <path d="M13 100 Q256 0 500 100 Q256 8 13 100 Z" fill="#111"/>
  </svg>
  <p class="sheet__site">WWW.NORTHVALELEND.COM</p>
</section>

</body>
</html>
```